Help me make landing pages for my web application that are mobile friendly

I need to make 2 mobile friendly landing pages for an application. The 2 pages will be related. First I need a home page and then I need a working page. I do not want to change the color scheme or logos. Just layout and design.

```html
<!DOCTYPE html>
<html lang="en">
<head>
<meta charset="utf-8">
<title>SwiftCover – My Assignment</title>
<link rel="stylesheet" href="https://fonts.googleapis.com/css2?family=Nunito+Sans:wght@400;600;700&display=swap">
<style>
:root{
  --page:#ffffff;
  --surface:#ffffff;
  --list-bg:#f5f8fd;
  --brand:#6a4fc0;
  --accent:#1ea6cc;
  --ink:#23262d;
  --muted:#878c95;
  --chip:#f1f2f4;
  --active-bg:#e2f4ea;--active-ink:#3a9d68;
  --done-bg:#e1f1fc;--done-ink:#2295c8;
  --cancel-bg:#fbe6eb;--cancel-ink:#b06e7c;
  --edit-off:#a9adb4;
}
*{box-sizing:border-box;margin:0;padding:0}
html,body{width:1200px;height:791px;overflow:hidden;background:var(--page)}
body{font-family:"Nunito Sans",sans-serif;color:var(--ink);position:relative}

.screen{position:absolute;top:118px;width:323px;height:490px;background:var(--list-bg);border-radius:14px;overflow:hidden;box-shadow:0 4px 22px rgba(60,80,140,.10)}
.screen--home{left:52px}
.screen--work{left:433px}
.screen--menu{left:813px}

.topbar{position:relative;z-index:3;height:45px;background:var(--surface);display:flex;align-items:center;justify-content:space-between;padding:0 23px 0 17px}
.screen--work .topbar{box-shadow:0 4px 10px rgba(60,80,140,.06)}
.brand{display:flex;align-items:center;gap:7px;font-size:17px;font-weight:600;color:var(--brand);letter-spacing:-.1px}
.brand-dot{width:12px;height:12px;border-radius:50%;background:var(--brand)}
.topbar-title{font-size:15.5px;font-weight:400;padding-left:2px}
.icon-btn{width:18px;height:18px;display:block}

.page-head{height:45px;display:flex;justify-content:space-between;align-items:center;padding:0 22px 0 19px}
.page-title{font-size:15.5px;font-weight:400}

.list{display:flex;flex-direction:column;gap:13px;padding:2px 14px 0}
.screen--work .list{margin-top:-63px;padding-top:0}

.card{position:relative;height:163px;flex-shrink:0;background:var(--surface);border-radius:9px;padding:15.5px 10px 0 79px}
.avatar{position:absolute;left:21px;top:20px;width:41px;height:41px;border-radius:50%;background:linear-gradient(160deg,#c9d3df,#8b97a6)}
.avatar--warm{background:linear-gradient(160deg,#e4d2c4,#a88672)}
.avatar--dark{background:linear-gradient(160deg,#b7bcc2,#5e6369)}
.edit{position:absolute;left:35px;top:74px;width:13px;height:14px;color:var(--accent)}
.edit--off{color:var(--edit-off)}

.top-row{display:flex}
.who{width:106px}
.label{font-size:9px;line-height:12px;color:var(--muted)}
.name{font-size:11.3px;line-height:16px;font-weight:600;color:var(--accent);margin-top:2.5px}
.role{font-size:10.5px;line-height:16px}
.status{display:inline-block;height:20px;line-height:20px;font-size:8.6px;letter-spacing:1.2px;padding:0 8px;border-radius:10px;margin-top:3px}
.status--active{background:var(--active-bg);color:var(--active-ink)}
.status--done{background:var(--done-bg);color:var(--done-ink)}
.status--cancel{background:var(--cancel-bg);color:var(--cancel-ink)}
.label--gap{margin-top:10px}
.value{font-size:11px;line-height:16px;margin-top:2px}
.slots{display:flex;gap:4px;margin-top:3px}
.slot{height:20px;line-height:20px;font-size:8.8px;letter-spacing:.9px;background:var(--chip);padding:0 8px;border-radius:10px}

.menu{position:relative;z-index:2;height:210px;background:var(--surface);display:flex;flex-direction:column;align-items:center;padding-top:14px;gap:16px;box-shadow:0 8px 12px rgba(60,80,140,.06);margin-bottom:13px}
.menu a{text-decoration:none;font-size:15.5px;line-height:20px;color:var(--brand);display:flex;align-items:center;gap:6px}
.menu a.current{color:var(--ink)}
.menu .list{padding-top:0}
.screen--menu .list{padding-top:0}
</style>
</head>
<body>

<section class="screen screen--home">
  <header class="topbar">
    <div class="brand"><span class="brand-dot"></span>SwiftCover</div>
    <svg class="icon-btn" viewBox="0 0 18 18" fill="none" stroke="var(--brand)" stroke-width="1.5"><path d="M1 4h16M1 9h16M1 14h16"/></svg>
  </header>
  <div class="page-head">
    <h1 class="page-title">My Assignment</h1>
    <svg class="icon-btn" viewBox="0 0 20 20" fill="none" stroke="var(--brand)" stroke-width="1.4"><path d="M4 3h12a2 2 0 0 1 2 2v8a2 2 0 0 1-2 2h-4l-2 3-2-3H4a2 2 0 0 1-2-2V5a2 2 0 0 1 2-2z"/><path d="M8 7.5a2 2 0 1 1 2.6 1.9c-.4.2-.6.5-.6.9v.3"/><circle cx="10" cy="12.4" r=".4" fill="var(--brand)"/></svg>
  </div>
  <div class="list">
    <article class="card">
      <div class="avatar" role="img" aria-label="Portrait of the teacher"></div>
      <svg class="edit" viewBox="0 0 13 14" fill="none" stroke="currentColor" stroke-width="1"><path d="M2.5 9.5l1-3 5-5 2 2-5 5zM1 13h11"/></svg>
      <div class="top-row"><div class="who"><p class="label">Subbing for :</p><p class="name">Noah Ellison</p><p class="role">Teacher</p></div><div><p class="label">Status :</p><span class="status status--active">ACTIVE</span></div></div>
      <p class="label label--gap">Location :</p><p class="value">Demo Valley Elementary Schools</p>
      <p class="label label--gap">Time Slots :</p><div class="slots"><span class="slot">09/02 - 09/18</span><span class="slot">1h : 20m</span></div>
    </article>
    <article class="card">
      <div class="avatar avatar--warm" role="img" aria-label="Portrait of the teacher"></div>
      <svg class="edit" viewBox="0 0 13 14" fill="none" stroke="currentColor" stroke-width="1"><path d="M2.5 9.5l1-3 5-5 2 2-5 5zM1 13h11"/></svg>
      <div class="top-row"><div class="who"><p class="label">Subbing for :</p><p class="name">Clara Whitfield</p><p class="role">Teacher</p></div><div><p class="label">Status :</p><span class="status status--done">COMPLETED</span></div></div>
      <p class="label label--gap">Location :</p><p class="value">Demo Valley Elementary Schools</p>
      <p class="label label--gap">Time Slots :</p><div class="slots"><span class="slot">09/02 - 09/18</span><span class="slot">1h : 20m</span></div>
    </article>
    <article class="card">
      <div class="avatar avatar--dark" role="img" aria-label="Portrait of the staff member"></div>
      <div class="top-row"><div class="who"><p class="label">Subbing for :</p><p class="name">Extra Duty</p><p class="role">Teacher</p></div><div><p class="label">Status :</p><span class="status status--cancel">CANCELED</span></div></div>
    </article>
  </div>
</section>

<section class="screen screen--work">
  <header class="topbar">
    <h1 class="topbar-title">My Assignment</h1>
    <svg class="icon-btn" viewBox="0 0 18 18" fill="none" stroke="var(--brand)" stroke-width="1.5"><path d="M1 4h16M1 9h16M1 14h16"/></svg>
  </header>
  <div class="list">
    <article class="card">
      <div class="avatar avatar--warm" role="img" aria-label="Portrait of the teacher"></div>
      <svg class="edit" viewBox="0 0 13 14" fill="none" stroke="currentColor" stroke-width="1"><path d="M2.5 9.5l1-3 5-5 2 2-5 5zM1 13h11"/></svg>
      <div class="top-row"><div class="who"><p class="label">Subbing for :</p><p class="name">Clara Whitfield</p><p class="role">Teacher</p></div><div><p class="label">Status :</p><span class="status status--done">COMPLETED</span></div></div>
      <p class="label label--gap">Location :</p><p class="value">Demo Valley Elementary Schools</p>
      <p class="label label--gap">Time Slots :</p><div class="slots"><span class="slot">09/02 - 09/18</span><span class="slot">1h : 20m</span></div>
    </article>
    <article class="card">
      <div class="avatar avatar--warm" role="img" aria-label="Portrait of the teacher"></div>
      <svg class="edit" viewBox="0 0 13 14" fill="none" stroke="currentColor" stroke-width="1"><path d="M2.5 9.5l1-3 5-5 2 2-5 5zM1 13h11"/></svg>
      <div class="top-row"><div class="who"><p class="label">Subbing for :</p><p class="name">Clara Whitfield</p><p class="role">Teacher</p></div><div><p class="label">Status :</p><span class="status status--done">COMPLETED</span></div></div>
      <p class="label label--gap">Location :</p><p class="value">Demo Valley Elementary Schools</p>
      <p class="label label--gap">Time Slots :</p><div class="slots"><span class="slot">09/02 - 09/18</span><span class="slot">1h : 20m</span></div>
    </article>
    <article class="card">
      <div class="avatar avatar--dark" role="img" aria-label="Portrait of the staff member"></div>
      <svg class="edit edit--off" viewBox="0 0 13 14" fill="none" stroke="currentColor" stroke-width="1"><path d="M2.5 9.5l1-3 5-5 2 2-5 5zM1 13h11"/></svg>
      <div class="top-row"><div class="who"><p class="label">Subbing for :</p><p class="name">Extra Duty</p><p class="role">Teacher</p></div><div><p class="label">Status :</p><span class="status status--cancel">CANCELED</span></div></div>
      <p class="label label--gap">Location :</p><p class="value">Demo Valley Elementary Schools</p>
      <p class="label label--gap">Time Slots :</p><div class="slots"><span class="slot">09/02 - 09/18</span><span class="slot">1h : 20m</span></div>
    </article>
  </div>
</section>

<section class="screen screen--menu">
  <header class="topbar">
    <div class="brand"><span class="brand-dot"></span>SwiftCover</div>
    <svg class="icon-btn" viewBox="0 0 18 18" fill="none" stroke="var(--brand)" stroke-width="1.4"><path d="M3 3l12 12M15 3L3 15"/></svg>
  </header>
  <nav class="menu">
    <a class="current" href="#">My Assignment</a>
    <a href="#">Available Opening</a>
    <a href="#">Support</a>
    <a href="#">Settings</a>
    <a href="#"><svg width="16" height="16" viewBox="0 0 16 16" fill="none" stroke="var(--brand)" stroke-width="1.2"><path d="M6 2h8v12H6M1.5 8h8M7 5.5L9.5 8 7 10.5"/></svg>Logout</a>
  </nav>
  <div class="list">
    <article class="card">
      <div class="avatar avatar--warm" role="img" aria-label="Portrait of the teacher"></div>
      <svg class="edit" viewBox="0 0 13 14" fill="none" stroke="currentColor" stroke-width="1"><path d="M2.5 9.5l1-3 5-5 2 2-5 5zM1 13h11"/></svg>
      <div class="top-row"><div class="who"><p class="label">Subbing for :</p><p class="name">Clara Whitfield</p><p class="role">Teacher</p></div><div><p class="label">Status :</p><span class="status status--done">COMPLETED</span></div></div>
      <p class="label label--gap">Location :</p><p class="value">Demo Valley Elementary Schools</p>
      <p class="label label--gap">Time Slots :</p><div class="slots"><span class="slot">09/02 - 09/18</span><span class="slot">1h : 20m</span></div>
    </article>
    <article class="card">
      <div class="avatar avatar--dark" role="img" aria-label="Portrait of the staff member"></div>
      <div class="top-row"><div class="who"><p class="label">Subbing for :</p><p class="name">Extra Duty</p><p class="role">Teacher</p></div><div><p class="label">Status :</p><span class="status status--cancel">CANCELED</span></div></div>
    </article>
  </div>
</section>

</body>
</html>
```